I need a SEO-friendly Wordpress website (making sure to style H1, H2, H3, etc correctly) for a Hawaii-based law firm called Meridian Crest Legal Group. Comparable websites include https://trvlaw.example/ and https://www.boultem.example/ for design reference. The current copy on the WelbyCounsel.example website can be used.

Coding

```html
<!DOCTYPE html>
<html lang="en">
<head>
<meta charset="utf-8">
<title>Welby Counsel – Meridian Crest Legal Group</title>
<link rel="stylesheet" href="https://fonts.googleapis.com/css2?family=Lora:ital,wght@0,400;0,700;1,400&family=Open+Sans:wght@400;600;700&display=swap">
<style>
:root{
  --brown:#7b2b0e;
  --brown-dark:#5e1f08;
  --orange:#e5892d;
  --ink:#2b2b2b;
  --muted:#6b6b6b;
  --blush:#fbf1ee;
  --white:#ffffff;
}
*{box-sizing:border-box;margin:0;padding:0}
html,body{width:1200px;height:2932px;overflow:hidden}
body{font-family:"Open Sans",Arial,sans-serif;color:var(--ink);background:var(--white);position:relative}
h1,h2,h3,.brand{font-family:"Lora",Georgia,serif}

/* header */
.site-header{position:absolute;top:0;left:0;width:1200px;height:112px;background:var(--white)}
.brand{position:absolute;left:108px;top:22px;font-size:38px;color:var(--brown);font-weight:400}
.call-tab{position:absolute;right:0;top:0;width:310px;height:44px;background:var(--brown);color:var(--white);font-size:17px;font-weight:600;display:flex;align-items:center;justify-content:center;clip-path:polygon(0 0,100% 0,100% 100%,8% 100%)}
.main-nav{position:absolute;right:90px;top:72px;display:flex;gap:46px;font-size:13px;font-weight:700;letter-spacing:.5px}
.main-nav a{color:var(--ink);text-decoration:none}
.main-nav a.active{color:var(--brown);border-bottom:2px solid var(--brown);padding-bottom:4px}

/* hero */
.hero{position:absolute;top:112px;left:0;width:1200px;height:708px;overflow:hidden}
.hero-photo{position:absolute;inset:0;background:linear-gradient(120deg,#4b3a30 0%,#7d6552 35%,#9a8a78 55%,#3d2c22 100%)}
.hero-shade{position:absolute;inset:0;background:rgba(30,18,12,.45)}
.hero-copy{position:absolute;top:390px;left:0;width:100%;text-align:center;color:var(--white)}
.hero-copy h1{font-size:54px;font-weight:700;color:var(--orange);letter-spacing:1px}
.hero-copy p{font-family:"Lora",Georgia,serif;font-style:italic;font-size:24px;margin-top:10px}
.btn-outline{display:inline-block;margin-top:40px;border:2px solid var(--white);border-radius:30px;padding:14px 36px;color:var(--white);font-size:15px;font-weight:600;letter-spacing:1px;text-decoration:none}

/* about */
.about{position:absolute;top:820px;left:0;width:1200px;height:500px}
.about h2{position:absolute;left:160px;top:66px;width:300px;font-size:46px;font-weight:400;line-height:1.3;color:var(--ink)}
.about h2 em{color:var(--orange);white-space:nowrap}
.about-text{position:absolute;left:472px;top:60px;width:690px;font-size:15px;line-height:1.75;color:var(--muted)}
.about-text p+p{margin-top:22px}
.btn-solid{display:inline-block;background:var(--brown);color:var(--white);border-radius:30px;padding:14px 38px;font-size:16px;text-decoration:none}
.about .btn-solid{position:absolute;left:472px;top:408px}

/* practice */
.practice{position:absolute;top:1320px;left:0;width:1200px;height:620px;background:var(--blush)}
.practice h2{text-align:center;font-size:50px;font-weight:400;color:var(--brown);margin-top:60px}
.cards{position:absolute;top:180px;left:112px;display:flex;gap:16px}
.card{width:232px;height:340px;background:var(--white);box-shadow:0 3px 10px rgba(0,0,0,.08)}
.card-photo{height:190px}
.card h3{font-size:19px;font-weight:700;text-align:center;margin-top:22px}
.card p{font-size:13px;line-height:1.6;color:var(--muted);text-align:center;padding:10px 16px 0}

/* attorneys */
.attorneys{position:absolute;top:1940px;left:0;width:1200px;height:652px}
.portrait-frame{position:absolute;left:168px;top:90px;width:370px;height:510px;border:4px solid var(--brown)}
.portrait{position:absolute;left:148px;top:110px;width:370px;height:510px;background:linear-gradient(160deg,#8c7a6a,#3b3431 60%,#6e5d50)}
.attorneys-copy{position:absolute;left:620px;top:130px;width:470px}
.attorneys-copy h2{font-size:30px;font-weight:400;line-height:1.3;letter-spacing:1px}
.attorneys-copy h2 strong{display:block;font-size:38px;color:var(--brown);font-weight:400}
.attorneys-copy p{margin-top:26px;font-size:14px;line-height:1.75;color:var(--muted)}
.attorneys-copy .btn-solid{margin-top:34px}

/* footer */
.site-footer{position:absolute;top:2592px;left:0;width:1200px;height:340px;background:var(--brown);color:var(--white)}
.footer-brand{text-align:center;font-family:"Lora",Georgia,serif;font-size:44px;padding-top:48px}
.footer-rule{width:1040px;height:1px;background:rgba(255,255,255,.35);margin:22px auto 0}
.contacts{display:flex;justify-content:space-between;width:1000px;margin:50px auto 0}
.contact{display:flex;gap:18px;align-items:flex-start;width:300px}
.contact svg{flex:none}
.contact h3{font-family:"Open Sans",Arial,sans-serif;font-size:17px;font-weight:700;margin-bottom:6px}
.contact p{font-size:13px;line-height:1.6}
.copyright{position:absolute;bottom:24px;width:100%;text-align:center;font-size:13px;opacity:.85}
</style>
</head>
<body>

<header class="site-header">
  <div class="brand">Welby Counsel</div>
  <div class="call-tab">Call Today: +1.808.555.0142</div>
  <nav class="main-nav">
    <a class="active" href="#">HOME</a>
    <a href="#">PRACTICE AREAS</a>
    <a href="#">ATTORNEYS</a>
    <a href="#">BLOG</a>
    <a href="#">CONTACT US</a>
  </nav>
</header>

<section class="hero">
  <div class="hero-photo" role="img" aria-label="Lawyers in suits reviewing documents with a client at an office table"></div>
  <div class="hero-shade"></div>
  <div class="hero-copy">
    <h1>MERIDIAN CREST LEGAL GROUP</h1>
    <p>Kona Lawyers of MCLG – Legal kōkua with aloha</p>
    <a class="btn-outline" href="#">LEARN MORE</a>
  </div>
</section>

<section class="about">
  <h2>About the <em>Kona Lawyers</em> of MCLG</h2>
  <div class="about-text">
    <p>The experienced attorneys at Meridian Crest Legal Group's Kailua-Kona, Hawaii office provide clients with a wide range of litigation expertise, including legal matters involving divorce &amp; family, personal injury, loan repayment, intellectual property and real estate.</p>
    <p>Our Kona office also offers commercial and hospitality litigation expertise on behalf of a wide variety of clients, including restaurants, hotels, property owners, and many others. We never wish to see our clients go to court, though if there is no other option, you're in safe hands with our seasoned trial lawyers and the many years of courtroom experience behind them.</p>
    <p>Kailua-Kona serves as the firm's West Coast headquarters for litigation and representation on behalf of individuals and corporations involved in a wide range of legal matters.</p>
  </div>
  <a class="btn-solid" href="#">Read More</a>
</section>

<section class="practice">
  <h2>Our Practice Area</h2>
  <div class="cards">
    <article class="card">
      <div class="card-photo" role="img" aria-label="Family with children sitting together" style="background:linear-gradient(135deg,#c9a98c,#8a6a55)"></div>
      <h3>Family &amp; Divorce</h3>
      <p>Our lawyers handle all aspects of family law on the Big Island and neighboring islands.</p>
    </article>
    <article class="card">
      <div class="card-photo" role="img" aria-label="Client shaking hands with a lawyer across a desk" style="background:linear-gradient(135deg,#d8d4cc,#8c8780)"></div>
      <h3>Personal Injury</h3>
      <p>Dealing with personal injury and wrongful death matters from strong on the lawyers of MCLG.</p>
    </article>
    <article class="card">
      <div class="card-photo" role="img" aria-label="Business team meeting around a table" style="background:linear-gradient(135deg,#b7b9bd,#5d6268)"></div>
      <h3>Corporate &amp; IP</h3>
      <p>The attorneys at MCLG have been helping Big Island business owners with all their legal needs.</p>
    </article>
    <article class="card">
      <div class="card-photo" role="img" aria-label="Agent handing house keys to buyers" style="background:linear-gradient(135deg,#d9c9b3,#94806a)"></div>
      <h3>Real Estate</h3>
      <p>Our lawyers work with home owners, buyers and property developers to secure their goals.</p>
    </article>
  </div>
</section>

<section class="attorneys">
  <div class="portrait-frame"></div>
  <div class="portrait" role="img" aria-label="Portrait of the firm's lead attorney in a dark suit"></div>
  <div class="attorneys-copy">
    <h2>ATTORNEYS of <strong>KONA-BASED MCLG</strong></h2>
    <p>Daniel Ashford is a graduate of the Halemano School of Law and later completed advanced study in international law. Over a long career he has worked as a personal injury lawyer, a family law practitioner and real estate counsel, serving as general counsel for hospitality businesses across the islands. He also holds a real estate broker license and has been based in Kailua-Kona for many years, where he leads the firm's litigation practice and mentors its younger attorneys.</p>
    <a class="btn-solid" href="#">Read More</a>
  </div>
</section>

<footer class="site-footer">
  <div class="footer-brand">Welby Counsel</div>
  <div class="footer-rule"></div>
  <div class="contacts">
    <div class="contact">
      <svg width="36" height="36" viewBox="0 0 36 36"><circle cx="18" cy="18" r="17" fill="none" stroke="#fff" stroke-width="2"/><path d="M18 9a6 6 0 0 0-6 6c0 5 6 12 6 12s6-7 6-12a6 6 0 0 0-6-6z" fill="#fff"/><circle cx="18" cy="15" r="2.2" fill="#7b2b0e"/></svg>
      <div><h3>Address:</h3><p>41-210 Makana Road, Suite 12<br>Kailua-Kona, Hawaii 96740</p></div>
    </div>
    <div class="contact">
      <svg width="36" height="36" viewBox="0 0 36 36"><circle cx="18" cy="18" r="17" fill="none" stroke="#fff" stroke-width="2"/><path d="M12 10l4 0 2 5-2.5 1.5a11 11 0 0 0 4 4L21 18l5 2v4c0 1-1 2-2 2C16 26 10 20 10 12c0-1 1-2 2-2z" fill="#fff"/></svg>
      <div><h3>Phone:</h3><p>+1.808.555.0142</p></div>
    </div>
    <div class="contact">
      <svg width="36" height="36" viewBox="0 0 36 36"><circle cx="18" cy="18" r="17" fill="none" stroke="#fff" stroke-width="2"/><rect x="10" y="12" width="16" height="12" fill="#fff"/><path d="M10 12l8 7 8-7" fill="none" stroke="#7b2b0e" stroke-width="1.5"/></svg>
      <div><h3>Email :</h3><p>clients@welbycounsel.example</p></div>
    </div>
  </div>
  <div class="copyright">© 2019 Welby Counsel All Rights Reserved</div>
</footer>

</body>
</html>
```